Flyer-Design für ein Restaurant
Zielgruppe
Wir betreiben ein Hotel im höchsten Wintersportort Österreichs – auf 2020 Meter Seehöhe.
Im Hotel ist ein Restaurant, welches abends geöffnet hat.
Wir legen im Restaurant sehr viel wert darauf, dass alles frisch gekocht wird und keinerlei Fertig-Produkte verarbeitet werden. Außerdem haben wir einen Holzkohlegrill wo die Steaks auf offenem Feuer gegrillt werden.
Vielleicht kann man irgendwie ein Foto von Feuer / Holzkohle oder so einbauen.
Im Ort gibt es allerhand Ferienwohnungen und auch Mitarbeiter die gerne am Abend essen gehen möchten.
genau das ist unser Klientel, das wir ansprechen möchten.
Die Flyer werden in den Betrieben wie Sportgeschäften / Skischulen etc. aufgelegt
Der Flyer soll durch seine Aufmachung / Design / Fotos den Wunsch wachsen lassen, dass man dort mal Essen gehen muss !
Aufgabenstellung
Wir haben uns für das quadratische Format 148 x 148mm entschieden – also ein Falzflyer mit 4 Seiten.
Falls man den Inhalt nicht auf 4 Seiten unterbringt, dann auch mit 6 Seiten möglich
Druckvorgabe liegt als Datei bei
Auf alle Fälle sollte im Flyer enthalten sein:
• Logo
• Telefonnummer für Tischreservierung (+43/5127/3861-417)
• Karte wie man uns findet
• Foto vom Hotel
• Adresse (Bergblick Residenz - Almrosenweg 9 - 6471 Lerchfeld)
• Auszüge aus der Speisekarte (ohne Preise) (Speisekarte ist als PDF dabei)
• Öffnungszeiten 18:00 – 21:00
• Kindergerichte
Ich werde unter der Adresse www.talvoro-demo.ag/flyer/
etliche Fotos hochladen vom Haus...daraus können Sie das ideale Foto raussuchen
Unsere Homepage ist www.bergwerkel.at - Muss aber nicht im Design oder dgl. zusammenpassen - ist eh schon alt !
Drucken lassen wir es bei druckvelo.at
Druckhinweise: https://www.druckvelo.at/p/falzflyer-a5-quadrat

```html
<!DOCTYPE html>
<html lang="de">
<head>
<meta charset="utf-8">
<title>Tilda's Restaurant – Falzflyer</title>
<link href="https://fonts.googleapis.com/css2?family=Cinzel:wght@400;600&family=Poppins:wght@400;600&display=swap" rel="stylesheet">
<style>
  :root {
    --stage: #d2d3d5;
    --paper: #ffffff;
    --brand: #5e4a3e;
    --ink: #2e2a28;
    --slate: #3b3b3d;
    --mocha: #6a5445;
    --line: #6b5a4e;
    --light: #f2efe9;
  }
  * { box-sizing: border-box; margin: 0; padding: 0; }
  html, body { width: 904px; height: 1200px; overflow: hidden; background: var(--stage); }
  body { position: relative; font-family: "Poppins", sans-serif; color: var(--ink); }

  .spread { position: absolute; left: 105px; width: 694px; height: 348px; background: var(--paper); overflow: hidden; }
  .spread--cover { top: 32px; }
  .spread--menu { top: 426px; }
  .spread--kids { top: 820px; }

  .panel { position: absolute; top: 0; height: 100%; }
  .abs { position: absolute; }

  .wordmark { font-family: "Cinzel", serif; color: var(--brand); font-weight: 400; text-align: center; line-height: 1; }
  .wordmark__name { display: block; }
  .wordmark__sub { display: block; letter-spacing: 0.18em; }
  .caps { font-family: "Cinzel", serif; color: var(--brand); font-weight: 600; }

  .section-title {
    position: absolute; left: 0;
    font-family: "Cinzel", serif; font-weight: 600; color: var(--brand);
    font-size: 7.2px; line-height: 1.05;
    border-bottom: 0.7px solid var(--line); padding-bottom: 1px;
  }
  .on-dark .section-title { color: #fff; border-color: #ddd; }

  .col { position: absolute; width: 112px; }
  .dish { margin-bottom: 6px; }
  .dish__name { font-family: "Cinzel", serif; font-weight: 600; color: var(--brand); font-size: 7.4px; line-height: 1.05; }
  .dish__desc { font-size: 5.2px; line-height: 1.3; color: var(--ink); }
  .dish__price { font-size: 5.2px; text-align: right; color: var(--ink); line-height: 1.3; }
  .dish__bold { font-weight: 600; font-size: 4.6px; }
  .person { font-size: 11px; color: var(--ink); line-height: 1; margin-bottom: 4px; }
  .person small { display: block; font-size: 7.5px; }

  .on-dark .dish__name, .on-dark .dish__desc, .on-dark .dish__price { color: #fff; }

  .photo { position: absolute; }
  .frame { position: absolute; border: 0.7px solid rgba(255,255,255,0.85); pointer-events: none; }
</style>
</head>
<body>

<section class="spread spread--cover">
  <div class="panel" style="left:0;width:347px;">
    <div class="photo" role="img" aria-label="Foto des Hotels im verschneiten Bergdorf"
         style="left:0;top:0;width:347px;height:185px;background:linear-gradient(180deg,#b9c7d8 0%,#dfe6ee 35%,#7d6a5e 60%,#e9edf1 100%);clip-path:polygon(0 0,100% 0,100% 145px,88% 140px,77% 160px,62% 140px,48% 185px,34% 150px,24% 150px,15% 118px,0 155px);"></div>

    <div class="wordmark abs" style="left:26px;top:210px;width:72px;">
      <span class="wordmark__name" style="font-size:21px;">TILDA'S</span>
      <span class="wordmark__sub" style="font-size:6px;margin-top:2px;">RESTAURANT</span>
    </div>

    <div class="caps abs" style="left:26px;top:253px;font-size:9.5px;line-height:1.2;">
      Bergblick Residenz<br>Almrosenweg 9<br>6471 Lerchfeld
    </div>

    <div class="caps abs" style="left:26px;top:309px;font-size:6px;">Für Tischreservierung</div>
    <div class="abs" style="left:26px;top:316px;font-family:'Cinzel',serif;color:var(--brand);font-size:14px;">+43 5127 3861 417</div>

    <div class="photo" role="img" aria-label="Lageplan mit Straßen und Liften, Standort des Restaurants markiert"
         style="left:142px;top:185px;width:186px;height:157px;background:radial-gradient(ellipse at center,#f3f4f6 0%,#fafafa 70%,#ffffff 100%);"></div>
  </div>

  <div class="panel" style="left:347px;width:347px;">
    <div class="wordmark abs" style="left:113px;top:52px;width:120px;">
      <span class="wordmark__name" style="font-size:31px;">TILDA'S</span>
      <span class="wordmark__sub" style="font-size:8px;margin-top:3px;">RESTAURANT</span>
    </div>
    <svg class="abs" style="left:87px;top:108px;" width="174" height="10" viewBox="0 0 174 10">
      <line x1="0" y1="5" x2="174" y2="5" stroke="#6b5a4e" stroke-width="0.8"/>
    </svg>

    <div class="photo" role="img" aria-label="Gebratene Kartoffeln mit Pilzen und Frühlingszwiebeln in der Pfanne"
         style="left:0;top:117px;width:347px;height:231px;background:radial-gradient(ellipse at 55% 60%,#b8782c 0%,#7a4a1c 45%,#2a1b12 80%,#1a120c 100%);clip-path:polygon(0 33px,77px 0,110px 30px,140px 45px,175px 68px,215px 52px,245px 38px,270px 27px,310px 4px,347px 32px,347px 231px,0 231px);"></div>
    <div class="frame" style="left:7px;top:160px;width:333px;height:181px;border-top:none;"></div>

    <div class="caps abs" style="left:0;width:347px;text-align:center;top:122px;font-size:6.5px;">Öffnungszeiten</div>
    <div class="abs" style="left:0;width:347px;text-align:center;top:130px;font-family:'Cinzel',serif;color:var(--brand);font-size:15px;">18:00 – 21:00</div>

    <div class="abs" style="left:120px;top:316px;width:108px;height:26px;background:var(--paper);text-align:center;padding-top:4px;">
      <div class="caps" style="font-size:4.8px;">Für Tischreservierung</div>
      <div style="font-family:'Cinzel',serif;color:var(--brand);font-size:11px;line-height:1.1;">+43 5127 3861 417</div>
    </div>
  </div>
</section>

<section class="spread spread--menu">
  <div class="panel" style="left:0;width:347px;">
    <div class="wordmark abs" style="left:145px;top:12px;width:56px;">
      <span class="wordmark__name" style="font-size:14px;">TILDA'S</span>
      <span class="wordmark__sub" style="font-size:4px;margin-top:1px;">RESTAURANT</span>
    </div>
    <div class="abs" style="left:130px;top:48px;width:88px;text-align:center;font-family:'Cinzel',serif;font-weight:600;color:var(--brand);font-size:12px;border-bottom:0.8px solid var(--line);padding-bottom:2px;">Speisekarte</div>

    <div class="section-title" style="top:80px;width:105px;padding-left:30px;">Die beliebtesten<br>Speisen von</div>
    <div class="col" style="left:30px;top:114px;">
      <div class="person">Marlene</div>
      <div class="dish">
        <div class="dish__name">Carpaccio mit Trüffel-Tagliolini</div>
        <div class="dish__desc">ein original sizilianisches Rezept verfeinert mit Rucola &amp; Parmesan</div>
        <div class="dish__price">€ 0.00</div>
      </div>
    </div>
    <div class="col" style="left:30px;top:183px;">
      <div class="person">Severin</div>
      <div class="dish">
        <div class="dish__name">Fischsuppe</div>
        <div class="dish__desc">klare Tomaten-Safransuppe mit Gemüse, verschiedenen Fischfilets, Muscheln, Meeresfrüchten, Aioli - dazu Knoblauchbrot</div>
        <div class="dish__price">€ 0.00</div>
      </div>
    </div>
    <div class="col" style="left:30px;top:257px;">
      <div class="person"><small>den Kindern</small>Fini &amp; Jakob</div>
      <div class="dish">
        <div class="dish__name">Hausgemachte Ravioli</div>
        <div class="dish__desc">gefüllt mit weißem Schoko-Mousse dazu eine edle Honig-Feigen-Sauce – Das perfekte Dessert –</div>
        <div class="dish__price">€ 0.00</div>
      </div>
    </div>

    <div class="section-title" style="top:89px;left:174px;width:82px;padding-left:30px;">Vorspeisen</div>
    <div class="col" style="left:204px;top:107px;">
      <div class="dish">
        <div class="dish__name">Carpaccio vom Tiroler Weiderind</div>
        <div class="dish__desc">Trüffelcreme, Parmesansplitter, hausgemachtes Brot</div>
        <div class="dish__price">€ 0.00</div>
      </div>
      <div class="dish">
        <div class="dish__desc">Büffelmozzarella, Tomaten-Carpaccio, Basilikum-Pesto, Balsamico Glace, hausgemachtes Brot</div>
        <div class="dish__price">€ 0.00</div>
      </div>
      <div class="dish">
        <div class="dish__name">Vitello Tonnato</div>
        <div class="dish__desc">rosa Kalbfleisch-Scheiben, Thunfischcreme, Rucola, Tomatencreme, Kapern, hausgemachtes Brot</div>
        <div class="dish__price">€ 0.00</div>
      </div>
    </div>
    <div class="section-title" style="top:226px;left:174px;width:82px;padding-left:30px;">Suppen</div>
    <div class="col" style="left:204px;top:242px;">
      <div class="dish">
        <div class="dish__name">Tomatencremesuppe</div>
        <div class="dish__desc">Basilikum / Croutons<br>(auch vegan möglich)</div>
        <div class="dish__price">€ 0.00</div>
      </div>
      <div class="dish">
        <div class="dish__name">Cremesüppchen vom Muskatkürbis</div>
        <div class="dish__desc">Kokos / Crouton</div>
        <div class="dish__price">€ 0.00</div>
      </div>
      <div class="dish">
        <div class="dish__name">Rindssuppe</div>
        <div class="dish__desc">mit Kräuter-Frittaten</div>
        <div class="dish__price">€ 0.00</div>
      </div>
    </div>
  </div>

  <div class="panel on-dark" style="left:347px;width:174px;background:var(--slate);">
    <div class="section-title" style="top:10px;width:58px;padding-left:31px;">Salate</div>
    <div class="col" style="left:31px;top:26px;">
      <div class="dish">
        <div class="dish__desc">kleiner gemischter Salat</div>
        <div class="dish__price">€ 0.00</div>
      </div>
      <div class="dish">
        <div class="dish__name">Cesar Salat</div>
        <div class="dish__desc">Das Original / Parmesansplitter / Croutons</div>
        <div class="dish__desc dish__bold">mit gegrillter Hühnerbrust &nbsp; mit Knoblauchgarnelen</div>
        <div class="dish__price">€ 0.00</div>
      </div>
      <div class="dish">
        <div class="dish__name">Bowl</div>
        <div class="dish__desc">Zupfsalat / Brinen / Schafskäse / getrocknete Tomaten / Cous Cous / crispy Bacon</div>
        <div class="dish__price">€ 0.00</div>
      </div>
    </div>
    <div class="section-title" style="top:131px;width:122px;padding-left:31px;">Pasta / Fisch &amp; mehr</div>
    <div class="col" style="left:31px;top:149px;">
      <div class="dish">
        <div class="dish__name">Hausgemachte Schlutzkrapfen</div>
        <div class="dish__desc">Teigtaschen gefüllt mit Ricotta, dazu Wildkräutersalat / Parmesan / braune Butter</div>
        <div class="dish__desc dish__bold">3 Stück &nbsp;&nbsp;&nbsp;&nbsp;&nbsp;&nbsp;&nbsp;&nbsp; 6 Stück &nbsp;&nbsp;&nbsp;&nbsp;&nbsp;&nbsp;&nbsp; € 0.00</div>
      </div>
      <div class="dish">
        <div class="dish__name">Conchiglioni</div>
        <div class="dish__desc">Muschelnudeln / Erbsencreme / Kohlrabiwürfel / Zuckerschoten</div>
        <div class="dish__price">€ 0.00</div>
      </div>
      <div class="dish">
        <div class="dish__name">Spaghetti Bolognese</div>
        <div class="dish__price">€ 0.00</div>
      </div>
      <div class="dish">
        <div class="dish__name">Saiblingsfilet</div>
        <div class="dish__desc">Kross gebraten aus Ötztaler Gewässern Tagliatelle / Fenchel / Lauch / Zitrone / Frischkäse / Spinatblätter Kapern / Tomatenflocken</div>
        <div class="dish__price">€ 0.00</div>
      </div>
      <div class="dish">
        <div class="dish__name">Carpaccio mit Trüffel-Tagliolini</div>
        <div class="dish__desc">ein original sizilianisches Rezept verfeinert mit Rucola &amp; Parmesan</div>
        <div class="dish__price">€ 0.00</div>
      </div>
    </div>
  </div>

  <div class="panel" style="left:521px;width:173px;">
    <div class="photo" role="img" aria-label="Burger mit Rindfleisch, Käse, Tomate und Salat"
         style="left:0;top:0;width:173px;height:147px;background:radial-gradient(ellipse at 50% 50%,#c98a3a 0%,#7b4a1f 50%,#3a2714 100%);"></div>
    <div class="frame" style="left:4px;top:3px;width:165px;height:141px;"></div>
    <div class="section-title" style="top:155px;left:0;width:92px;padding-left:30px;">Hauptspeisen</div>
    <div class="col" style="left:30px;top:173px;width:125px;">
      <div class="dish">
        <div class="dish__name">Wiener Schnitzel<br>vom Schwein</div>
        <div class="dish__desc">mit Pommes frites und Preiselbeeren</div>
        <div class="dish__price">€ 0.00</div>
      </div>
      <div class="dish">
        <div class="dish__name">Residenz Burger</div>
        <div class="dish__desc">Rindfleisch, Speck, Gurken, rote Zwiebel, Tomaten, Salat, Sauce, Bacon und Pommes frites</div>
        <div class="dish__price">€ 0.00</div>
      </div>
      <div class="dish">
        <div class="dish__name">Fischsuppe</div>
        <div class="dish__desc">klare Tomaten-Safransuppe mit Gemüse, verschiedenen Fischfilets, Muscheln, Meeresfrüchten, Aioli - dazu Knoblauchbrot</div>
        <div class="dish__price">€ 0.00</div>
      </div>
      <div class="dish">
        <div class="dish__name">Veganer Burger</div>
        <div class="dish__desc">Veganes Patty / Tomate / Salat / rote Zwiebel / Wakame Alge Limetten-Aioli und Pommes frites</div>
        <div class="dish__price">€ 0.00</div>
      </div>
    </div>
  </div>
</section>

<section class="spread spread--kids">
  <div class="panel" style="left:0;width:173px;">
    <div class="photo" role="img" aria-label="Glühende Holzkohle mit offenem Feuer"
         style="left:0;top:0;width:173px;height:170px;background:radial-gradient(ellipse at 50% 55%,#e2541c 0%,#8e2a10 40%,#2a0d08 75%,#120606 100%);"></div>
    <div class="frame" style="left:4px;top:4px;width:165px;height:162px;"></div>
    <div class="section-title" style="top:184px;width:150px;padding-left:30px;">Aus dem Holzkohlegrill<br>bei offenem Feuer und 350°</div>
    <div class="col" style="left:30px;top:208px;width:122px;">
      <div class="dish" style="display:flex;gap:10px;margin-bottom:4px;">
        <div style="flex:1;"><div class="dish__name">Filetsteak</div><div class="dish__desc">250g &nbsp;&nbsp;&nbsp;&nbsp;&nbsp; € 0.00</div></div>
        <div style="flex:1;"><div class="dish__name">Ribeysteak</div><div class="dish__desc">300g &nbsp;&nbsp;&nbsp;&nbsp;&nbsp;&nbsp; € 0.00</div></div>
      </div>
      <div class="dish">
        <div class="dish__desc dish__bold">Alle Steaks servieren wir mit</div>
        <div class="dish__desc">Gemüse / Pommes frites / 2 kalte Saucen / Kräuterbutter</div>
        <div class="dish__price">€ 0.00</div>
      </div>
      <div class="dish">
        <div class="dish__name">Tagliata</div>
        <div class="dish__desc">250g vom Rumpsteak</div>
        <div class="dish__desc dish__bold">in Streifen geschnitten dazu</div>
        <div class="dish__desc">Rucola / Kirschtomaten / Parmesan</div>
        <div class="dish__price">€ 0.00</div>
      </div>
      <div class="dish">
        <div class="dish__name">Schweinerückensteak</div>
        <div class="dish__desc">Senfsauce / Gemüse / Pommes frites</div>
        <div class="dish__price">€ 0.00</div>
      </div>
    </div>
  </div>

  <div class="panel" style="left:173px;width:174px;">
    <div class="section-title" style="top:20px;width:126px;padding-left:31px;">Fini &amp; Jakob empfehlen</div>
    <div class="col" style="left:31px;top:30px;">
      <div class="dish__desc" style="margin-bottom:5px;">Kindergerichte</div>
      <div class="dish"><div class="dish__name">Feuerwehrteller „Funki“</div><div class="dish__desc">Schnitzel mit Pommes</div><div class="dish__price">€ 0.00</div></div>
      <div class="dish"><div class="dish__name">Flocke</div><div class="dish__desc">Spaghetti Bolognese</div><div class="dish__price">€ 0.00</div></div>
      <div class="dish"><div class="dish__name">Rudi</div><div class="dish__desc">Muschelnudeln mit Tomatensauce</div><div class="dish__price">€ 0.00</div></div>
      <div class="dish"><div class="dish__name">Fischli</div><div class="dish__desc">gegrilltes Saiblingsfilet mit Gemüse</div><div class="dish__price">€ 0.00</div></div>
      <div class="dish"><div class="dish__name">Räuberteller</div><div class="dish__desc">Leerer Teller zum Mitnaschen</div><div class="dish__price">€ 0.00</div></div>
      <div class="dish"><div class="dish__name">Bodo der Bauarbeiter</div><div class="dish__desc">Portion Pommes</div><div class="dish__price">€ 0.00</div></div>
    </div>
    <div class="photo" role="img" aria-label="Kind isst Spaghetti mit Tomatensauce"
         style="left:0;top:212px;width:174px;height:136px;background:linear-gradient(160deg,#dfe7ee 0%,#9fb4c8 45%,#3e6a98 75%,#d0623a 100%);"></div>
  </div>

  <div class="panel on-dark" style="left:347px;width:174px;background:var(--mocha);">
    <div class="section-title" style="top:20px;width:70px;padding-left:31px;">Dessert</div>
    <div class="col" style="left:31px;top:38px;">
      <div class="dish"><div class="dish__name">Halbflüssiges Schokoküchlein</div><div class="dish__desc">mit Birnenragout &amp; Tonkabohnen-Eis</div><div class="dish__price">€ 0.00</div></div>
      <div class="dish"><div class="dish__name">Creme Brûlée</div><div class="dish__desc">Kirsch-Crumble &amp; Sauerrahm-Eis</div><div class="dish__price">€ 0.00</div></div>
      <div class="dish"><div class="dish__name">Dreierlei Schokoladenmousse</div><div class="dish__desc">mit Himbeersauce &amp; Salz-Karamel-Eis</div><div class="dish__price">€ 0.00</div></div>
      <div class="dish"><div class="dish__name">Hausgemachte Ravioli</div><div class="dish__desc">gefüllt mit weißem Schoko-Mousse dazu eine edle Honig-Feigen-Sauce</div><div class="dish__price">€ 0.00</div></div>
      <div class="dish"><div class="dish__name">Kindereisbecher mit Schokolinsen</div><div class="dish__desc">Vanille- und Erdbeereis, Sahne und einer kleinen Überraschung</div><div class="dish__price">€ 0.00</div></div>
      <div class="dish"><div class="dish__name">Gemischtes Eis<br><span style="font-size:5.5px;">(3 Kugeln)</span></div><div class="dish__desc">Vanille, Erdbeere, Schokolade mit oder ohne Sahne</div><div class="dish__price">€ 0.00</div></div>
      <div class="dish"><div class="dish__name">Coupe Danmark</div><div class="dish__desc">Vanilleeis mit heißer Schokosauce und Sahne</div><div class="dish__price">€ 0.00</div></div>
      <div class="dish"><div class="dish__name">Heisse Liebe</div><div class="dish__desc">Cremiges Vanilleeis mit heißen Himbeeren und Sahne</div><div class="dish__price">€ 0.00</div></div>
    </div>
  </div>

  <div class="panel" style="left:521px;width:173px;">
    <div class="photo" role="img" aria-label="Gestapelte Brownies mit fließender Schokoladensauce und Minze"
         style="left:0;top:0;width:173px;height:348px;background:radial-gradient(ellipse at 50% 72%,#5a3320 0%,#2a1810 40%,#111 75%,#0b0b0b 100%);"></div>
    <div class="frame" style="left:4px;top:4px;width:165px;height:340px;"></div>
  </div>
</section>

</body>
</html>
```